Create the ONLY Supplement line for Male Entrepreneurs! (Veltro Prime MD)

I need a label designed for a new supplement brand that I am launching.

There are five products so need a design that I can simply change the wording for each individual product

The brand name is called veltro prime MD. The focus is male entrepreneurial health.

Target audience is men 35 to 55.

Concepts: the healthier you are in body the more money you will make in business.

Concept to copy: I want to make a clean minimalistic label mimicking Dallamore MD (google it and you'll see what I mean)

Target Market(s)

male entrepreneurs 35-55

Industry/Entity Type

Health Supplement

Colors

Designer to choose colors to be used in the design.

Requirements
Must have
• Modern classy design, similar to Dallamore MD.
Nice to have
• Highlight that the supplement is Doctor Approved.
Should not have
• No loud colors. Present it as high class.

```html
<!DOCTYPE html>
<html lang="en">
<head>
<meta charset="utf-8">
<title>Veltro Prime MD – Omega 3 Label</title>
<link rel="stylesheet" href="https://fonts.googleapis.com/css2?family=Montserrat:wght@400;500&family=Playfair+Display:wght@400&display=swap">
<style>
  :root {
    --page-bg: #01021c;
    --brand-navy: #14106a;
    --label-white: #ffffff;
    --accent-gold: #ef9608;
  }
  * { margin: 0; padding: 0; box-sizing: border-box; }
  html, body {
    width: 1200px;
    height: 768px;
    overflow: hidden;
    background: var(--page-bg);
  }
  .canvas {
    position: relative;
    width: 1200px;
    height: 768px;
    background: var(--page-bg);
  }
  .label {
    position: absolute;
    left: 414px;
    top: 130px;
    width: 372px;
    height: 509px;
    background: var(--label-white);
    overflow: hidden;
  }
  .label__wave {
    position: absolute;
    left: 0;
    top: 0;
    width: 372px;
    height: 190px;
  }
  .brand {
    position: absolute;
    left: 26px;
    top: 28px;
    color: var(--label-white);
  }
  .brand__name {
    font-family: "Playfair Display", serif;
    font-weight: 400;
    font-size: 44px;
    line-height: 1;
    letter-spacing: -0.01em;
    white-space: nowrap;
  }
  .brand__tagline {
    margin-top: 10px;
    font-family: "Montserrat", sans-serif;
    font-weight: 500;
    font-size: 16px;
    letter-spacing: 0.38em;
  }
  .product-figure {
    position: absolute;
    left: 16px;
    top: 246px;
    width: 132px;
    height: 80px;
    border-radius: 6px;
    background: linear-gradient(180deg, #e6e5f2 0%, #f4efe4 100%);
  }
  .product {
    position: absolute;
    left: 23px;
    top: 330px;
    color: var(--brand-navy);
  }
  .product__name {
    font-family: "Playfair Display", serif;
    font-weight: 400;
    font-size: 41px;
    line-height: 1.1;
  }
  .product__type,
  .product__count {
    font-family: "Montserrat", sans-serif;
    font-weight: 500;
    font-size: 17px;
    line-height: 1;
  }
  .product__type { margin-top: 8px; }
  .product__count { margin-top: 9px; }
  .approval-band {
    position: absolute;
    left: 0;
    top: 443px;
    width: 372px;
    height: 34px;
    background: var(--brand-navy);
    color: var(--label-white);
    font-family: "Montserrat", sans-serif;
    font-weight: 500;
    font-size: 16px;
    line-height: 34px;
    padding-left: 11px;
  }
  .approval-seal {
    position: absolute;
    left: 302px;
    top: 428px;
    width: 64px;
    height: 64px;
  }
</style>
</head>
<body>
<main class="canvas">
  <section class="label">
    <svg class="label__wave" viewBox="0 0 372 190" aria-hidden="true">
      <path fill="var(--brand-navy)" d="M0,139 C30,120 60,114 80,116 C130,118 170,145 220,165 C260,180 290,186 315,184 C345,182 362,170 372,159 V0 H0 Z"/>
    </svg>

    <header class="brand">
      <h1 class="brand__name">Veltro Prime MD</h1>
      <p class="brand__tagline">SUPPLEMENT</p>
    </header>

    <div class="product-figure" role="img" aria-label="Line illustration of a flexing muscular torso circled by a gold ring"></div>

    <div class="product">
      <h2 class="product__name">Omega 3</h2>
      <p class="product__type">Digtary supplement</p>
      <p class="product__count">90 softgels</p>
    </div>

    <p class="approval-band">Supplement is Doctor Approved</p>

    <svg class="approval-seal" viewBox="0 0 64 64" aria-hidden="true">
      <polygon fill="var(--accent-gold)" points="64,32 57.1,38.7 59.7,48 50.4,50.4 48,59.7 38.7,57.1 32,64 25.3,57.1 16,59.7 13.6,50.4 4.3,48 6.9,38.7 0,32 6.9,25.3 4.3,16 13.6,13.6 16,4.3 25.3,6.9 32,0 38.7,6.9 48,4.3 50.4,13.6 59.7,16 57.1,25.3"/>
      <polyline fill="none" stroke="var(--label-white)" stroke-width="5" stroke-linecap="round" stroke-linejoin="round" points="20,33 28,41 45,22"/>
    </svg>
  </section>
</main>
</body>
</html>
```